Sunk Deep

I am need a book cover with a beautiful African Portuguese set in the 1800's (Think Mary Thornwick, Salt and Silence). This is a Cinderella type story in which the hero and heroine are trapped in the cellar of a collapsed mansion. The story is set off the coast of Africa in the British Colony of Port of Elizabeth

Her dress can be colorful. Her hair can be up and spilling out. Please blow me away with this cover. I am attaching the first cover in this series.

```html
<!DOCTYPE html>
<html lang="en">
<head>
<meta charset="utf-8">
<title>Sunk Deep — Book Cover</title>
<link rel="stylesheet" href="https://fonts.googleapis.com/css2?family=Great+Vibes&family=Crimson+Text&display=swap">
<style>
  :root {
    --backdrop: #d9d9d9;
    --band: #4a4239;
    --band-deep: #2e2924;
    --author: #f1ece4;
    --gown-light: #9a4a2e;
    --gown-mid: #6a2417;
    --photo-deep: #2c0b07;
    --photo-black: #050303;
    --stair-light: #eeeeee;
    --stair-mid: #6e6e6e;
    --title: #ffffff;
    --title-shadow: #6b1512;
  }
  html, body {
    margin: 0;
    width: 1200px;
    height: 901px;
    overflow: hidden;
    background: var(--backdrop);
  }
  .cover {
    position: absolute;
    left: 366px;
    top: 72px;
    width: 468px;
    height: 756px;
    overflow: hidden;
    background: var(--photo-black);
  }
  .pattern-band {
    position: absolute;
    left: 0;
    top: 0;
    width: 468px;
    height: 92px;
    background: linear-gradient(90deg, var(--band-deep), var(--band) 50%, var(--band-deep));
  }
  .author {
    position: absolute;
    left: 0;
    top: 52px;
    width: 468px;
    margin: 0;
    text-align: center;
    font-family: "Crimson Text", Georgia, serif;
    font-size: 22px;
    line-height: 1;
    color: var(--author);
  }
  .cover-art {
    position: absolute;
    left: 0;
    top: 92px;
    width: 468px;
    height: 664px;
    background: var(--photo-black);
  }
  .heroine-photo {
    position: absolute;
    left: 0;
    top: 0;
    width: 330px;
    height: 664px;
    background:
      radial-gradient(ellipse 160px 300px at 110px 430px, var(--gown-light), var(--gown-mid) 45%, rgba(0,0,0,0) 100%),
      radial-gradient(ellipse 120px 140px at 150px 140px, var(--gown-mid), rgba(0,0,0,0) 100%),
      linear-gradient(90deg, var(--photo-deep), var(--photo-deep) 60%, var(--photo-black));
  }
  .stairwell-photo {
    position: absolute;
    left: 300px;
    top: 0;
    width: 168px;
    height: 340px;
    background:
      radial-gradient(ellipse 70px 90px at 60px 70px, var(--stair-light), var(--stair-mid) 55%, rgba(0,0,0,0) 100%),
      linear-gradient(180deg, #3a3a3a, var(--photo-black));
  }
  .title {
    position: absolute;
    left: 0;
    top: 0;
    margin: 0;
    font-family: "Great Vibes", cursive;
    font-weight: 400;
    color: var(--title);
    text-shadow: 3px 3px 0 var(--title-shadow);
  }
  .title span {
    position: absolute;
    white-space: nowrap;
    font-size: 128px;
    line-height: 1;
  }
  .title .line-one { left: 24px; top: 405px; }
  .title .line-two { left: 118px; top: 540px; }
</style>
</head>
<body>
  <main class="cover">
    <div class="pattern-band" role="img" aria-label="Dark geometric lattice pattern band"></div>
    <p class="author">Clara Whitlow</p>
    <div class="cover-art">
      <div class="heroine-photo" role="img" aria-label="Heroine in a flowing satin gown, glancing over her shoulder in a dark cellar"></div>
      <div class="stairwell-photo" role="img" aria-label="Cellar staircase rising toward a bright doorway"></div>
    </div>
    <h1 class="title">
      <span class="line-one">Sunk</span>
      <span class="line-two">Deep</span>
    </h1>
  </main>
</body>
</html>
```